Quillory Nest Business Card

I need a business card design. We are a collaborate online training company. Our colors are gray and green. Our website is QuilloryNest.com

I would like an area for a profile picture within the card

```html
<!DOCTYPE html>
<html lang="en">
<head>
<meta charset="utf-8">
<title>Quillory Nest Business Card</title>
<link rel="stylesheet" href="https://fonts.googleapis.com/css2?family=Source+Sans+3:wght@400;600;700&display=swap">
<style>
  :root {
    --stage: #000000;
    --card: #343538;
    --card-dark: #2d2e31;
    --green: #7ec440;
    --white: #ffffff;
    --text-soft: #e6e6e6;
    --divider: #45464a;
    --photo-top: #5a5b5f;
    --photo-bottom: #3b3c40;
  }
  * { margin: 0; padding: 0; box-sizing: border-box; }
  html, body { width: 1200px; height: 900px; overflow: hidden; background: var(--stage); }
  body { position: relative; font-family: "Source Sans 3", "Myriad Pro", sans-serif; }

  .card {
    position: absolute;
    top: 271px;
    width: 457px;
    height: 281px;
    border-radius: 12px;
    background: linear-gradient(180deg, var(--card) 0%, var(--card-dark) 100%);
    overflow: hidden;
  }
  .card-front { left: 137px; }
  .card-back { left: 626px; }

  .profile-photo {
    position: absolute;
    left: 0; top: 0;
    width: 222px; height: 281px;
    background: radial-gradient(ellipse at 50% 40%, var(--photo-top) 0%, var(--photo-bottom) 75%, transparent 100%);
  }

  .divider {
    position: absolute;
    left: 224px; top: 90px;
    width: 1px; height: 140px;
    background: var(--divider);
  }

  .details { position: absolute; left: 246px; top: 57px; color: var(--text-soft); }
  .name { font-size: 18px; font-weight: 600; color: var(--white); line-height: 22px; }
  .name .first { color: var(--green); }
  .role { font-size: 12.5px; line-height: 15px; }
  .address { margin-top: 21px; font-size: 12.5px; line-height: 14px; }
  .contacts { list-style: none; margin-top: 18px; font-size: 12.5px; }
  .contacts li { display: flex; align-items: center; height: 19px; }
  .contacts svg { width: 10px; height: 10px; margin-right: 5px; fill: var(--green); flex: none; }

  .brand {
    position: absolute;
    left: 0; right: 0; top: 105px;
    display: flex; align-items: center; justify-content: center; gap: 14px;
  }
  .brand-dot { width: 44px; height: 44px; border-radius: 50%; background: var(--green); }
  .brand-name { font-size: 46px; font-weight: 700; color: var(--white); letter-spacing: -1px; line-height: 1; }

  .web-rule {
    position: absolute;
    left: 0; right: 0; top: 243px;
    display: flex; align-items: center; gap: 6px;
    color: var(--green); font-size: 12.5px; font-weight: 700;
  }
  .web-rule::before, .web-rule::after { content: ""; flex: 1; height: 1.5px; background: var(--green); }
</style>
</head>
<body>
  <section class="card card-front">
    <div class="profile-photo" role="img" aria-label="Portrait photo of the managing director"></div>
    <div class="divider"></div>
    <div class="details">
      <p class="name"><span class="first">Dorian</span> Welkes</p>
      <p class="role">Managing Director</p>
      <p class="address">12345, Address Goes Here<br>Country Name, 123456</p>
      <ul class="contacts">
        <li><svg viewBox="0 0 10 10"><path d="M2 0.5 L3.6 2.6 L2.7 3.6 C3.3 5 4.9 6.6 6.4 7.3 L7.4 6.4 L9.5 8 L8.4 9.5 C4.5 9.3 0.7 5.5 0.5 1.6 Z"/></svg>(044)-456-7890</li>
        <li><svg viewBox="0 0 10 10"><path d="M3 0.5 H7 V3 H9.5 V9.5 H0.5 V3 H3 Z M4 1.5 V3 H6 V1.5 Z M2 5 V6 H4 V5 Z M5 5 V6 H8 V5 Z M2 7 V8 H8 V7 Z"/></svg>123-456-7890</li>
        <li><svg viewBox="0 0 10 10"><path d="M0.5 2 H9.5 V8.5 H0.5 Z M1.3 2.7 L5 5.4 L8.7 2.7 Z" fill-rule="evenodd"/></svg>info@youremail.com</li>
        <li><svg viewBox="0 0 10 10"><circle cx="5" cy="5" r="4.5"/><path d="M3 2 C4 3 3 4 4 5 C5 6 4 7 5 8.5 M6 1.5 C6.5 3 7.5 3 8.5 4" stroke="#343538" stroke-width="0.8" fill="none"/></svg>www.quillorynest.com</li>
      </ul>
    </div>
  </section>

  <section class="card card-back">
    <div class="brand">
      <span class="brand-dot"></span>
      <span class="brand-name">QuilloryNest</span>
    </div>
    <p class="web-rule">www.quillorynest.com</p>
  </section>
</body>
</html>
```